Business Card Design Project - bel soravin group

dear Sirs

we need business card design for our group ( BEL Soravin Group ) , i have got the Logo design of our group from pixel harbor in previous , so all need details relating to our group i think available with you, as well as the the chosen logo design

we hope to provide us with business card logo that to be appropaite and satisfactory to us .

thanks

note : logo design of our group is attached .
Updates

Reason: please extend the deadline of my project for additional 15 days because i didn't received appropriate design for our gruop yet . kindly beaware that i have received 77 design till now , supossed to send me 200-250 design at least . thanks

Target Market(s)

contents
-

name : Korvan EL Mistrani

position : Operation Manager

Industry/Entity Type

Business

Requirements
Must have

• person name

group logo
Nice to have
• logo color matching with back background

```html
<!DOCTYPE html>
<html lang="en">
<head>
<meta charset="utf-8">
<title>BEL Soravin Group – Business Card</title>
<link rel="stylesheet" href="https://fonts.googleapis.com/css2?family=Arimo:wght@400;700&display=swap">
<style>
  :root {
    --card-bg: #f1e4bf;
    --brand-blue: #0b4f8e;
    --accent-gold: #c9952e;
  }
  * { margin: 0; padding: 0; box-sizing: border-box; }
  html, body {
    width: 1200px;
    height: 750px;
    overflow: hidden;
    background: var(--card-bg);
  }
  .business-card {
    position: relative;
    width: 1200px;
    height: 750px;
    background: var(--card-bg);
    font-family: "Arimo", Arial, sans-serif;
    color: var(--brand-blue);
  }
  .brand-mark {
    position: absolute;
    left: 110px;
    top: 150px;
    width: 980px;
    height: 130px;
    display: flex;
    align-items: center;
    justify-content: center;
    gap: 28px;
  }
  .brand-mark__square {
    width: 62px;
    height: 62px;
    background: var(--accent-gold);
    flex: none;
  }
  .brand-mark__name {
    font-size: 84px;
    font-weight: 700;
    line-height: 1;
    color: var(--brand-blue);
    white-space: nowrap;
  }
  .holder {
    position: absolute;
    top: 356px;
    left: 0;
    width: 1200px;
    text-align: center;
  }
  .holder__name {
    font-size: 32px;
    font-weight: 700;
    line-height: 38px;
  }
  .holder__role {
    font-size: 25px;
    font-weight: 400;
    line-height: 30px;
  }
  .contact-list {
    position: absolute;
    left: 116px;
    top: 440px;
    list-style: none;
    font-size: 26px;
    line-height: 32.5px;
  }
  .website {
    position: absolute;
    top: 630px;
    left: 0;
    width: 1200px;
    text-align: center;
    font-size: 25px;
    letter-spacing: 0.42em;
  }
</style>
</head>
<body>
  <main class="business-card">
    <div class="brand-mark">
      <span class="brand-mark__square" aria-hidden="true"></span>
      <span class="brand-mark__name">BEL Soravin Group</span>
    </div>

    <section class="holder">
      <h1 class="holder__name">Korvan EL Mistrani</h1>
      <p class="holder__role">Operations Manager</p>
    </section>

    <ul class="contact-list">
      <li>Tel: 555.555.5555</li>
      <li>Fax: 555.55.5555</li>
      <li>Mobile: 555.555.5555</li>
      <li>E-mail: yourname@belsoravingroup.com</li>
      <li>PO. Box: addres here</li>
    </ul>

    <p class="website">www.belsoravingroup.com</p>
  </main>
</body>
</html>
```